Business Card Design Project

We need a business card design template for a direct sales company that is branded to the company but the name information can be changed for the representatives. The card needs to include the company logo and website...www.myvelsane.example. It should also include the Customer Service number which is 1-800-472-Velsan.

The front should have a space with the name and a place for their phone contact information and email address.
Updates

The card should be two sided.  It could also include the tagline "Velsane is all about V!" or any of the information from www.myvelsane.example.

I am uploading the other formats that I currently have for the logo.

Thank you

Target Market(s)

The representatives are teenage girls that are 13-19 but they are selling products to all ages.

Industry/Entity Type

Business

Requirements
Must have
• A field with the toll free customer service number.
The company logo.
The company website information.
The company representative name.
The company representative phone number.
The company representative email contact info.
Nice to have
• QR Code which we already have.
Should not have
• Do not make it look like a design for children. It should be modern and professional but sophisticated.

```html
<!DOCTYPE html>
<html lang="en">
<head>
<meta charset="utf-8">
<title>Velsane Business Card</title>
<link href="https://fonts.googleapis.com/css2?family=Tinos&display=swap" rel="stylesheet">
<style>
  :root {
    --backdrop: #5f4751;
    --card: #ffffff;
    --magenta: #d6217f;
    --pink-deep: #e0277f;
    --pink-soft: #f49ac4;
    --arc: #f3c9a6;
    --shadow: rgba(0, 0, 0, 0.25);
  }
  * { margin: 0; padding: 0; box-sizing: border-box; }
  html, body {
    width: 1200px;
    height: 900px;
    overflow: hidden;
    background: var(--backdrop);
    font-family: "Tinos", "Times New Roman", serif;
  }
  .stage { position: relative; width: 1200px; height: 900px; }
  .card {
    position: absolute;
    top: 316px;
    width: 474px;
    height: 264px;
    background: var(--card);
    border-radius: 16px;
    overflow: hidden;
  }
  .card--front { left: 116px; }
  .card--back { left: 610px; }
  .card__arc { position: absolute; inset: 0; width: 100%; height: 100%; }
  .card__tiles {
    position: absolute;
    top: 0;
    right: 0;
    width: 104px;
    height: 264px;
    background: linear-gradient(200deg, var(--pink-deep) 0%, var(--pink-soft) 45%, rgba(244, 154, 196, 0.25) 80%, rgba(255, 255, 255, 0) 100%);
  }
  .brand {
    position: absolute;
    left: 46px;
    top: 54px;
    display: flex;
    align-items: center;
    gap: 10px;
    color: var(--magenta);
    font-size: 36px;
    line-height: 1;
  }
  .brand__mark {
    width: 13px;
    height: 13px;
    background: var(--magenta);
  }
  .rep-name {
    position: absolute;
    left: 70px;
    top: 130px;
    color: var(--magenta);
    font-size: 21px;
    line-height: 24px;
  }
  .contact {
    position: absolute;
    left: 70px;
    top: 164px;
    list-style: none;
    color: var(--magenta);
    font-size: 18px;
    line-height: 23px;
  }
  .tagline {
    position: absolute;
    left: 50px;
    top: 106px;
    color: var(--magenta);
    font-size: 36px;
    line-height: 1.2;
    white-space: nowrap;
    text-shadow: 2px 6px 4px var(--shadow);
  }
</style>
</head>
<body>
<main class="stage">
  <section class="card card--front">
    <svg class="card__arc" viewBox="0 0 474 264" aria-hidden="true">
      <path d="M14 264 C 60 150, 150 40, 330 0" fill="none" stroke="var(--arc)" stroke-width="1.5"/>
    </svg>
    <div class="card__tiles" role="img" aria-label="Cascade of pink and magenta squares along the right edge"></div>
    <div class="brand">
      <span class="brand__mark"></span>
      <span class="brand__name">Velsane</span>
    </div>
    <p class="rep-name">Vera Lindqvist</p>
    <ul class="contact">
      <li>Phone: 1-800-472-Velsan</li>
      <li>www.myvelsane.example</li>
      <li>Mail: vera@myvelsane.example</li>
    </ul>
  </section>

  <section class="card card--back">
    <svg class="card__arc" viewBox="0 0 474 264" aria-hidden="true">
      <path d="M14 264 C 60 150, 150 40, 330 0" fill="none" stroke="var(--arc)" stroke-width="1.5"/>
    </svg>
    <div class="card__tiles" role="img" aria-label="Cascade of pink and magenta squares along the right edge"></div>
    <p class="tagline">“Velsane is all about V”</p>
  </section>
</main>
</body>
</html>
```